Marlowe Consulting Cover 2 - Bright Ledger

Marlowe Consulting is a business consulting firm. We will publish a series of four thought leadership pieces online and via PDF. The second of the series is attached to this project. We need an eye-catching cover page with a back page that keeps with our branding. The document attached is in the final draft, and the cover and pack pages are placeholders only. You can find more about our branding and style on our website www.marloweconsulting.com.au. The other three projects can be found here with a similar brief, and you are welcome to submit a design for all 4.

```html
<!DOCTYPE html>
<html lang="en">
<head>
<meta charset="utf-8">
<title>Marlowe Consulting – Bright Ledger cover</title>
<link rel="stylesheet" href="https://fonts.googleapis.com/css2?family=Poppins:wght@400;500;600;700;800&display=swap">
<style>
  :root {
    --stage: #a9a9a9;
    --label: #2b2b2b;
    --navy: #13427a;
    --navy-deep: #0f3b70;
    --orange: #f7931e;
    --sky-blue: #1aa3e8;
    --white: #ffffff;
  }
  * { box-sizing: border-box; margin: 0; padding: 0; }
  html, body { width: 1200px; height: 990px; overflow: hidden; }
  body {
    background: var(--stage);
    font-family: "Poppins", sans-serif;
    position: relative;
  }
  .side-label {
    position: absolute;
    top: 78px;
    width: 451px;
    text-align: center;
    font-weight: 600;
    font-size: 27px;
    color: var(--label);
    letter-spacing: 0.5px;
  }
  .side-label.back { left: 148px; }
  .side-label.front { left: 635px; }

  .page {
    position: absolute;
    top: 154px;
    width: 451px;
    height: 697px;
    overflow: hidden;
    box-shadow: 0 4px 14px rgba(0,0,0,0.18);
  }
  .page.back { left: 136px; }
  .page.front { left: 613px; }
  .page-art { position: absolute; inset: 0; width: 451px; height: 697px; }

  /* Back page */
  .contact-bubble {
    position: absolute;
    left: 150px; top: 78px;
    width: 254px; height: 254px;
    border-radius: 50%;
    background: var(--orange);
    border: 5px solid var(--white);
    display: flex; flex-direction: column; align-items: center; justify-content: center;
    text-align: center;
    color: var(--white);
    padding: 0 26px 12px;
  }
  .contact-tag {
    background: var(--sky-blue);
    border-radius: 12px;
    font-size: 12.5px; font-weight: 600;
    padding: 1px 9px;
    margin-bottom: 3px;
  }
  .contact-copy { font-size: 16.5px; font-weight: 600; line-height: 1.25; }

  .brand {
    position: absolute;
    display: flex; align-items: center;
    color: var(--orange);
    font-weight: 700;
    line-height: 1.0;
  }
  .brand .brand-dot { border-radius: 50%; background: var(--orange); flex: none; }
  .back .brand { left: 243px; top: 470px; font-size: 17px; gap: 9px; }
  .back .brand .brand-dot { width: 36px; height: 36px; }

  .person { position: absolute; top: 537px; color: var(--white); }
  .person.first { left: 62px; }
  .person.second { left: 242px; }
  .person-name { font-size: 17px; font-weight: 500; line-height: 1.2; }
  .person-role { font-size: 9.5px; font-weight: 500; letter-spacing: 2px; color: var(--sky-blue); margin-bottom: 6px; }
  .contact-line { display: flex; align-items: center; gap: 5px; line-height: 1.5; }
  .contact-line svg { width: 9px; height: 9px; flex: none; }
  .contact-line.phone { font-size: 12.5px; font-weight: 500; }
  .contact-line.email { font-size: 7.5px; }

  .follow {
    position: absolute; left: 66px; top: 624px;
    color: var(--white); font-size: 13.5px; font-weight: 500;
    display: flex; align-items: center; gap: 6px;
  }
  .follow .follow-dot { width: 15px; height: 15px; border-radius: 50%; background: var(--sky-blue); }

  .web {
    position: absolute; top: 634px;
    font-size: 12.5px; font-weight: 600; letter-spacing: 0.5px;
    color: var(--white);
  }
  .web span { color: var(--orange); }
  .back .web { left: 240px; }
  .front .web { left: 52px; }

  /* Front page */
  .front .brand { left: 46px; top: 108px; font-size: 26px; gap: 12px; }
  .front .brand .brand-dot { width: 54px; height: 54px; }

  .headline {
    position: absolute; left: 52px; top: 438px;
    font-size: 52px; font-weight: 800; line-height: 0.8;
    color: var(--orange); text-transform: uppercase; letter-spacing: -0.5px;
  }
  .subhead {
    position: absolute; left: 52px; top: 525px;
    color: var(--white); font-size: 21px; font-weight: 600; line-height: 1.05;
  }
  .tagline {
    position: absolute; left: 52px; top: 576px;
    color: var(--sky-blue); font-size: 15.5px; font-weight: 500;
  }
</style>
</head>
<body>
  <div class="side-label back">BACK</div>
  <div class="side-label front">FRONT</div>

  <section class="page back">
    <svg class="page-art" viewBox="0 0 451 697">
      <defs>
        <linearGradient id="back-photo" x1="0" y1="0" x2="1" y2="0.6">
          <stop offset="0" stop-color="#8fb4dc"/>
          <stop offset="0.45" stop-color="#c6d9ec"/>
          <stop offset="1" stop-color="#e4edf6"/>
        </linearGradient>
      </defs>
      <rect role="img" aria-label="Photo of a modern angular building with blue glass panels against a cloudy sky" width="451" height="697" fill="url(#back-photo)"/>
      <polygon points="0,510 451,310 451,697 0,697" fill="var(--white)"/>
      <polygon points="0,520 451,320 451,697 0,697" fill="var(--navy-deep)"/>
    </svg>

    <div class="contact-bubble">
      <span class="contact-tag">CONTACT US</span>
      <p class="contact-copy">to find out how Marlowe Consulting can help build your company into a market leader today.</p>
    </div>

    <div class="brand"><span class="brand-dot"></span><span>Marlowe<br>Consulting</span></div>

    <div class="person first">
      <div class="person-name">Henry Marlowe</div>
      <div class="person-role">MANAGING DIRECTOR</div>
      <div class="contact-line phone"><svg viewBox="0 0 10 10"><path d="M2 1l2 2-1 1c.6 1.2 1.6 2.2 3 3l1-1 2 2-1.2 1.2C4.5 9 1 5.5.8 2.2z" fill="var(--orange)"/></svg>+61 400 318 226</div>
      <div class="contact-line email"><svg viewBox="0 0 10 10"><rect x="0.5" y="2" width="9" height="6.5" rx="1" fill="var(--orange)"/><path d="M1 2.5l4 3 4-3" stroke="var(--navy-deep)" fill="none" stroke-width="0.8"/></svg>henry@marloweconsulting.com.au</div>
    </div>

    <div class="person second">
      <div class="person-name">Oliver Marlowe</div>
      <div class="person-role">MANAGING DIRECTOR</div>
      <div class="contact-line phone"><svg viewBox="0 0 10 10"><path d="M2 1l2 2-1 1c.6 1.2 1.6 2.2 3 3l1-1 2 2-1.2 1.2C4.5 9 1 5.5.8 2.2z" fill="var(--orange)"/></svg>+61 400 964 571</div>
      <div class="contact-line email"><svg viewBox="0 0 10 10"><rect x="0.5" y="2" width="9" height="6.5" rx="1" fill="var(--orange)"/><path d="M1 2.5l4 3 4-3" stroke="var(--navy-deep)" fill="none" stroke-width="0.8"/></svg>oliver@marloweconsulting.com.au</div>
    </div>

    <div class="follow">Follow us <span class="follow-dot"></span></div>
    <div class="web"><span>marloweconsulting</span>.com.au</div>
  </section>

  <section class="page front">
    <svg class="page-art" viewBox="0 0 451 697">
      <defs>
        <linearGradient id="front-photo" x1="0" y1="0" x2="1" y2="0.8">
          <stop offset="0" stop-color="#86b8e6"/>
          <stop offset="0.5" stop-color="#cfdeec"/>
          <stop offset="1" stop-color="#a9acb0"/>
        </linearGradient>
      </defs>
      <rect role="img" aria-label="Photo looking up at grey concrete buildings with stepped balconies against a blue sky" width="451" height="697" fill="url(#front-photo)"/>
      <polygon points="0,312 451,512 451,697 0,697" fill="var(--white)"/>
      <polygon points="0,322 451,522 451,697 0,697" fill="var(--navy)"/>
    </svg>

    <div class="brand"><span class="brand-dot"></span><span>Marlowe<br>Consulting</span></div>

    <h1 class="headline">Bright<br>Ledger</h1>
    <p class="subhead">Partnering with funds<br>to scale your business.</p>
    <p class="tagline">Bridging valuation gaps in fund raising</p>
    <div class="web"><span>marloweconsulting</span>.com.au</div>
  </section>
</body>
</html>
```